Elegant, professional powerpoint design for Brisval Engineering and Mining SARLU

I’ve created a new Sub contracting company for mining industry in the Democratic Republic of Congo. With Quillmoor, I’ve created a logo. I would want a professional and beautiful powerpoint design which I will use to sell my services to mining companies in DRC. The powerpoint must have pictures of mining engines such as excavators, drones, trucks, etc

```html
<!DOCTYPE html>
<html lang="en">
<head>
<meta charset="utf-8">
<title>Brisval Engineering and Mining — Presentation</title>
<link href="https://fonts.googleapis.com/css2?family=Krona+One&family=Poppins:wght@400;500;600;700&display=swap" rel="stylesheet">
<style>
:root{
  --stage:#7d7e80;
  --navy:#1b2a8f;
  --navy-deep:#16207a;
  --gold:#c98a12;
  --gold-light:#f3a81c;
  --gold-dark:#8a5410;
  --ink:#2b2b2b;
  --muted:#555;
  --white:#fff;
  --paper:#f1f0ee;
}
*{box-sizing:border-box;margin:0;padding:0}
html,body{width:1200px;height:4231px;overflow:hidden}
body{background:var(--stage);position:relative;font-family:"Poppins",sans-serif;color:var(--ink)}
.slide{position:absolute;left:59px;width:1080px;height:607px;overflow:hidden;background:var(--white)}
.heading{font-family:"Krona One",sans-serif;letter-spacing:2px}
.accent{color:var(--gold)}
.corner-mark{position:absolute;right:54px;top:42px;width:30px;height:30px;border-radius:4px;background:linear-gradient(160deg,var(--gold-light),var(--gold-dark))}
.brand-name{font-family:"Krona One",sans-serif;color:var(--navy);display:flex;align-items:center;gap:14px}
.brand-square{background:var(--gold);display:inline-block}
.brand-sub{font-family:"Krona One",sans-serif;color:var(--gold);letter-spacing:2px}

/* cover */
.cover{top:84px}
.cover svg{position:absolute;inset:0}
.cover .brand{position:absolute;left:56px;top:340px}
.cover .brand-name{font-size:40px}
.cover .brand-square{width:26px;height:26px}
.cover .brand-sub{font-size:15px;margin-top:12px}

/* about */
.about{top:760px;background:linear-gradient(120deg,#e9e7e4,#f3f1ee 45%,#e6e0d8)}
.about h2{position:absolute;top:42px;width:100%;text-align:center;font-size:27px;color:var(--navy)}
.about p{position:absolute;top:120px;left:146px;width:788px;text-align:center;font-size:11px;line-height:24px;color:var(--ink)}
.about .hex-photo{position:absolute;left:405px;top:310px}

/* industry */
.industry{top:1448px;background:#2a1a12}
.industry svg{position:absolute;inset:0}
.industry h2{position:absolute;left:52px;top:40px;font-size:26px;line-height:43px;color:var(--white)}
.industry .block{position:absolute;left:58px;width:470px;color:var(--white)}
.industry h3{font-size:15px;font-weight:500;color:var(--gold-light);margin-bottom:6px}
.industry ul{list-style:none}
.industry li{font-size:10.5px;line-height:19px;padding-left:16px;position:relative;margin-bottom:7px}
.industry li::before{content:"";position:absolute;left:0;top:6px;width:7px;height:7px;border-radius:50%;background:var(--white)}
.industry li b{font-weight:600}

/* partners */
.partners{top:2139px}
.partners h2{position:absolute;top:42px;width:100%;text-align:center;font-size:25px;color:var(--navy)}
.partner-grid{position:absolute;left:117px;top:177px;display:grid;grid-template-columns:repeat(4,184px);grid-auto-rows:82px;column-gap:37px;row-gap:25px}
.partner-card{background:var(--white);border-radius:12px;box-shadow:0 3px 10px rgba(0,0,0,.14);display:flex;align-items:center;justify-content:center}
.partner-badge{width:60px;height:36px;border-radius:6px;background:#d9dbe3}
.partner-badge.round{width:42px;height:42px;border-radius:50%}

/* team */
.team{top:2842px;background:linear-gradient(135deg,var(--navy) 0%,var(--navy-deep) 100%)}
.team h2{position:absolute;top:42px;width:100%;text-align:center;font-size:25px;color:var(--white)}
.member{position:absolute;top:169px;width:222px;text-align:center}
.member .portrait{display:block;width:212px;height:194px;margin:0 auto}
.member .name{background:var(--white);height:41px;line-height:41px;font-family:"Krona One",sans-serif;font-size:12.5px;color:var(--navy)}
.member p{margin-top:22px;font-size:10px;line-height:17px;color:#dfe3ff;padding:0 10px}
.socials{display:flex;justify-content:center;gap:15px;margin-top:20px}
.socials span{width:29px;height:29px;border-radius:50%;border:1.5px solid var(--gold)}

/* thanks */
.thanks{top:3538px;background:linear-gradient(135deg,#eef3f9,#ffffff 55%)}
.thanks h2{position:absolute;left:52px;top:200px;font-size:44px;color:transparent;-webkit-text-stroke:1.5px var(--navy);letter-spacing:3px}
.thanks h2 .accent{color:transparent;-webkit-text-stroke:1.5px var(--gold)}
.thanks .presenter{position:absolute;left:60px;top:302px;font-size:17px;font-weight:500;color:var(--ink)}
.contact{position:absolute;left:60px;top:352px;list-style:none;width:320px}
.contact li{display:flex;align-items:flex-start;gap:14px;font-size:11px;line-height:15px;color:var(--muted);margin-bottom:22px}
.contact svg{flex:none;width:16px;height:16px;fill:var(--navy)}
.thanks .brand{position:absolute;left:555px;top:380px;text-align:center}
.thanks .brand-name{font-size:48px}
.thanks .brand-square{width:30px;height:30px}
.thanks .brand-sub{font-size:19px;margin-top:14px}
</style>
</head>
<body>

<section class="slide cover">
  <svg width="1080" height="607" viewBox="0 0 1080 607">
    <defs>
      <linearGradient id="goldBand" x1="0" y1="0" x2="0.3" y2="1">
        <stop offset="0" stop-color="#7a4a0e"/><stop offset="1" stop-color="#f7ab1c"/>
      </linearGradient>
      <linearGradient id="landscape" x1="0" y1="0" x2="0" y2="1">
        <stop offset="0" stop-color="#c9ccd0"/><stop offset="0.35" stop-color="#7f9a86"/><stop offset="0.6" stop-color="#6c8c44"/><stop offset="1" stop-color="#4e7228"/>
      </linearGradient>
    </defs>
    <polygon points="507,0 1080,0 1080,607 633,607 675,318" fill="url(#landscape)" role="img" aria-label="Photo of green hills above a river and a Congolese town"/>
    <polygon points="290,0 507,0 675,318 470,318" fill="var(--navy)"/>
    <polygon points="470,318 675,318 507,607 298,607" fill="url(#goldBand)"/>
  </svg>
  <div class="brand">
    <div class="brand-name"><span class="brand-square"></span>BRISVAL</div>
    <div class="brand-sub">ENGINEERING AND MINING</div>
  </div>
</section>

<section class="slide about">
  <h2 class="heading">ABOUT <span class="accent">US</span></h2>
  <span class="corner-mark"></span>
  <p>Lorem ipsum dolor sit amet, consectetur adipiscing elit, sed do eiusmod tempor incididunt ut labore et dolore magna aliqua. Ut enim ad minim veniam, quis nostrud exercitation ullamco laboris nisi ut aliquip ex ea commodo consequat. Duis aute irure dolor in reprehenderit in voluptate velit esse cillum dolore eu fugiat nulla pariatur. Excepteur sint occaecat cupidatat non proident, sunt in culpa qui officia deserunt mollit anim id est laborum.Sed ut perspiciatis unde omnis iste natus error sit voluptatem accusantium doloremque laudantium, nesciunt. Neque porro quisquam est, qui dolorem ipsum quia dolor sit amet, consectetur, adipisci velit, sed quia non numquam eius modi tempora incidunt ut labore et dolore magnam aliquam quaerat voluptatem.</p>
  <svg class="hex-photo" width="270" height="280" viewBox="0 0 270 280" role="img" aria-label="Photo of tropical palms and a lakeside building inside a hexagon frame">
    <defs><linearGradient id="forest" x1="0" y1="0" x2="0" y2="1"><stop offset="0" stop-color="#6f8f4a"/><stop offset="0.6" stop-color="#2f5a2a"/><stop offset="1" stop-color="#4a6a6a"/></linearGradient></defs>
    <polygon points="135,0 270,70 270,210 135,280 0,210 0,70" fill="url(#forest)"/>
  </svg>
</section>

<section class="slide industry">
  <svg width="1080" height="607" viewBox="0 0 1080 607">
    <defs>
      <linearGradient id="tunnel" x1="0" y1="0" x2="1" y2="1"><stop offset="0" stop-color="#5a3020"/><stop offset="0.5" stop-color="#7a4a30"/><stop offset="1" stop-color="#3a2016"/></linearGradient>
    </defs>
    <rect x="440" y="0" width="640" height="607" fill="url(#tunnel)" role="img" aria-label="Photo of a miner in a hard hat standing in an underground tunnel"/>
    <polygon points="0,0 466,0 619,607 0,607" fill="var(--navy)"/>
    <line x1="466" y1="0" x2="619" y2="607" stroke="#fff" stroke-width="3"/>
  </svg>
  <span class="corner-mark"></span>
  <h2 class="heading">BRISVAL MINING<br>INDUSTRY</h2>
  <div class="block" style="top:168px">
    <h3>The Future of the Brisval Mining Industry</h3>
    <ul>
      <li>Lorem ipsum dolor sit amet, consectetur adipiscing elit, sed do</li>
      <li>Excepteur sint occaecat cupidatat non proident, sunt in culpa qui officia deserunt</li>
      <li>Duis aute irure dolor in reprehenderit in voluptate velit esse cillum</li>
    </ul>
  </div>
  <div class="block" style="top:292px">
    <h3>Brisval Mining Industry – Congo Mine Services</h3>
    <ul>
      <li>Ut enim ad minim veniam, quis nostrud exercitation</li>
      <li>Sed ut perspiciatis unde omnis iste natus error sit voluptatem accusantium doloremque laudantium, totam rem aperiam.</li>
      <li>Nemo enim ipsam voluptatem quia voluptas sit</li>
      <li>Neque porro quisquam est, qui dolorem ipsum quia dolor sit amet, consectetur</li>
      <li><b>RENEWABLE FUTURE:</b> Ut enim ad minima veniam, quis nostrum exercitationem ullam corporis suscipit laboriosam, nisi ut aliquid ex ea commodi consequatur.</li>
    </ul>
  </div>
</section>

<section class="slide partners">
  <h2 class="heading">OUR <span class="accent">PARTNERS</span></h2>
  <span class="corner-mark"></span>
  <div class="partner-grid">
    <div class="partner-card"><span class="partner-badge" style="width:110px;height:26px"></span></div>
    <div class="partner-card"><span class="partner-badge round"></span></div>
    <div class="partner-card"><span class="partner-badge"></span></div>
    <div class="partner-card"><span class="partner-badge round"></span></div>
    <div class="partner-card"><span class="partner-badge"></span></div>
    <div class="partner-card"><span class="partner-badge round"></span></div>
    <div class="partner-card"><span class="partner-badge"></span></div>
    <div class="partner-card"><span class="partner-badge round"></span></div>
    <div class="partner-card"><span class="partner-badge round"></span></div>
    <div class="partner-card"><span class="partner-badge round"></span></div>
    <div class="partner-card"><span class="partner-badge" style="width:100px;height:30px"></span></div>
    <div class="partner-card"><span class="partner-badge round"></span></div>
  </div>
</section>

<section class="slide team">
  <h2 class="heading">OUR TEAM</h2>
  <span class="corner-mark"></span>
  <div class="member" style="left:54px">
    <svg class="portrait" viewBox="0 0 212 194" role="img" aria-label="Portrait of a smiling engineer in a yellow hard hat"><rect width="212" height="194" fill="#8a8f96"/></svg>
    <div class="name">Jhon Smith</div>
    <p>Lorem ipsum dolor sit amet, consectetur adipiscing elit, sed do eiusmod tempor ut aliquip ex ea commodo consequat.</p>
    <div class="socials"><span></span><span></span><span></span><span></span></div>
  </div>
  <div class="member" style="left:303px">
    <svg class="portrait" viewBox="0 0 212 194" role="img" aria-label="Portrait of a female engineer in a hard hat and safety vest"><rect width="212" height="194" fill="#9a8a78"/></svg>
    <div class="name">Jhon Smith</div>
    <p>Lorem ipsum dolor sit amet, consectetur adipiscing elit, sed do eiusmod tempor ut aliquip ex ea commodo consequat.</p>
    <div class="socials"><span></span><span></span><span></span><span></span></div>
  </div>
  <div class="member" style="left:553px">
    <svg class="portrait" viewBox="0 0 212 194" role="img" aria-label="Portrait of an engineer in a white hard hat in a plant"><rect width="212" height="194" fill="#5f7484"/></svg>
    <div class="name">Jhon Smith</div>
    <p>Lorem ipsum dolor sit amet, consectetur adipiscing elit, sed do eiusmod tempor ut aliquip ex ea commodo consequat.</p>
    <div class="socials"><span></span><span></span><span></span><span></span></div>
  </div>
  <div class="member" style="left:803px">
    <svg class="portrait" viewBox="0 0 212 194" role="img" aria-label="Portrait of a female worker in a hi-vis vest holding a tablet"><rect width="212" height="194" fill="#6e6a5a"/></svg>
    <div class="name">Jhon Smith</div>
    <p>Lorem ipsum dolor sit amet, consectetur adipiscing elit, sed do eiusmod tempor ut aliquip ex ea commodo consequat.</p>
    <div class="socials"><span></span><span></span><span></span><span></span></div>
  </div>
</section>

<section class="slide thanks">
  <h2 class="heading">THANK <span class="accent">YOU</span></h2>
  <div class="presenter">PRESENTER NAME</div>
  <ul class="contact">
    <li><svg viewBox="0 0 24 24"><path d="M6.6 10.8a15 15 0 0 0 6.6 6.6l2.2-2.2a1 1 0 0 1 1-.25 11.4 11.4 0 0 0 3.6.57 1 1 0 0 1 1 1V20a1 1 0 0 1-1 1A17 17 0 0 1 3 4a1 1 0 0 1 1-1h3.5a1 1 0 0 1 1 1c0 1.25.2 2.45.57 3.57a1 1 0 0 1-.25 1z"/></svg>+1 (888) 888 888</li>
    <li><svg viewBox="0 0 24 24"><path d="M12 2a10 10 0 1 0 0 20 10 10 0 0 0 0-20zm6.9 6h-3a15.6 15.6 0 0 0-1.4-3.6A8 8 0 0 1 18.9 8zM12 4c.8 1.2 1.5 2.5 1.9 4h-3.8c.4-1.5 1.1-2.8 1.9-4zM4.3 14a8 8 0 0 1 0-4h3.4a16 16 0 0 0 0 4zm.8 2h3a15.6 15.6 0 0 0 1.4 3.6A8 8 0 0 1 5.1 16zm3-8h-3a8 8 0 0 1 4.4-3.6A15.6 15.6 0 0 0 8.1 8zM12 20c-.8-1.2-1.5-2.5-1.9-4h3.8c-.4 1.5-1.1 2.8-1.9 4zm2.3-6H9.7a14.7 14.7 0 0 1 0-4h4.6a14.7 14.7 0 0 1 0 4zm.2 5.6a15.6 15.6 0 0 0 1.4-3.6h3a8 8 0 0 1-4.4 3.6zm1.8-5.6a16 16 0 0 0 0-4h3.4a8 8 0 0 1 0 4z"/></svg>www.brisval.com</li>
    <li><svg viewBox="0 0 24 24"><path d="M2 5h20v14H2zm2 2v.5l8 5 8-5V7zm0 2.9V17h16V9.9l-8 5z"/></svg>info@brisval.com</li>
    <li><svg viewBox="0 0 24 24"><path d="M12 2a7 7 0 0 0-7 7c0 5.2 7 13 7 13s7-7.8 7-13a7 7 0 0 0-7-7zm0 9.5A2.5 2.5 0 1 1 12 6.5a2.5 2.5 0 0 1 0 5z"/></svg>123,Lorem ipsum dolor sit amet, consectetur adipiscing elit</li>
  </ul>
  <div class="brand">
    <div class="brand-name"><span class="brand-square"></span>BRISVAL</div>
    <div class="brand-sub">ENGINEERING AND MINING</div>
  </div>
</section>

</body>
</html>
```